Welding and farication business card

Business name Tbm Welding & Fabrication

I need a business card made for my welding and fabrication business that is bold and stands out. My business is both welding repairs on machinery and anything else you can imagine as well as fabricating new products. i have used this service before and was very happy with the out come of my design logo. i think the card should remain fairly simple and classy but also be bold. I think a black card would best be suited to the talk with my logo on it. i feel the back of the card should just have my logo and the front have my logo email, website and phone number and maybe incorporate a facebook and instagram simple if it can be made look good these arnt a necessity.
I have included both my logo and some business card ideas below

Target Market(s)

Farmers, heavy industry, earthmoving, trucking

Industry/Entity Type

Engineering

Contact Information for Business Card

0438517264
dale@tbmweldingandfabrication.com.au
www.tbmweldingandfabrication.com.au

Colors
33a6d7
0255a3

Requirements
Must have
• Dale Hutchins
my phone number 0438517264
my logo
Preferably a black card desgn
Nice to have
• List of what i do,
Sheds and carports
Ute trays
Stockyards
Trailers
Farm equipment
Stockcrates
Gateways and Entrances
Breakdowns
Maintenance
And lots more!

```html
<!DOCTYPE html>
<html lang="en">
<head>
<meta charset="utf-8">
<title>Tbm Welding &amp; Fabrication – Business Card</title>
<link rel="stylesheet" href="https://fonts.googleapis.com/css2?family=Montserrat:wght@500;600;700;800&display=swap">
<style>
  :root {
    --bg: #c9c9c9;
    --card: #141414;
    --blue: #0255a3;
    --sky: #33a6d7;
    --steel: #5d6b7a;
    --white: #ffffff;
    --muted: #d9dde2;
  }
  * { box-sizing: border-box; margin: 0; padding: 0; }
  html, body { width: 1200px; height: 788px; overflow: hidden; }
  body {
    background: var(--bg);
    font-family: "Montserrat", Arial, sans-serif;
    display: flex; align-items: center; justify-content: center; gap: 30px;
  }
  .card {
    position: relative; width: 560px; height: 320px;
    background: var(--card); border-radius: 22px; overflow: hidden;
    box-shadow: 0 10px 30px rgba(0,0,0,.25);
  }
  .wordmark {
    position: absolute; color: var(--blue); font-weight: 800;
    text-transform: uppercase; line-height: 1.05; letter-spacing: .02em;
  }
  .wordmark .mark-dot {
    display: inline-block; width: .45em; height: .45em; border-radius: 50%;
    background: var(--blue); margin-right: .3em; vertical-align: middle;
  }

  /* front */
  .card--front .wordmark { left: 38px; top: 112px; font-size: 22px; width: 190px; }
  .divider { position: absolute; left: 238px; top: 78px; width: 1px; height: 130px; background: var(--blue); }
  .contact { position: absolute; left: 262px; top: 72px; }
  .contact__name { color: var(--blue); font-weight: 700; font-size: 22px; letter-spacing: .04em; text-transform: uppercase; margin-bottom: 14px; }
  .contact__line { display: flex; align-items: center; gap: 8px; color: var(--white); font-size: 12px; font-weight: 500; margin-bottom: 7px; }
  .contact__line svg { width: 12px; height: 12px; fill: var(--sky); flex: none; }
  .wave { position: absolute; inset: 0; width: 100%; height: 100%; }
  .social { position: absolute; right: 34px; bottom: 34px; display: flex; align-items: center; gap: 8px; color: var(--white); font-size: 13px; font-weight: 600; }
  .social__dot { width: 10px; height: 10px; border-radius: 50%; background: var(--white); }

  /* back */
  .flare { position: absolute; left: 140px; top: 10px; width: 300px; height: 260px;
    background: radial-gradient(ellipse at center, rgba(70,90,110,.35), rgba(20,20,20,0) 65%); }
  .card--back .wordmark { left: 0; right: 0; top: 48px; text-align: center; font-size: 38px; }
  .services-rule { position: absolute; left: 0; right: 0; top: 186px; height: 1px; background: var(--blue); }
  .services-tag { position: absolute; left: 50%; top: 172px; transform: translateX(-50%);
    background: var(--blue); color: var(--white); font-weight: 800; font-size: 17px;
    padding: 4px 16px; border-radius: 16px; }
  .services { position: absolute; left: 20px; right: 20px; top: 222px; text-align: center; list-style: none; }
  .services li { display: inline; color: var(--white); font-size: 13px; font-weight: 600; margin: 0 5px; line-height: 2; }
  .services li::before { content: "•"; color: var(--sky); margin-right: 4px; }
</style>
</head>
<body>

<section class="card card--front" aria-label="Card front">
  <svg class="wave" viewBox="0 0 560 320" preserveAspectRatio="none" aria-hidden="true">
    <path d="M0 320 L560 320 L560 150 C470 175 420 260 300 296 C200 320 80 300 0 320 Z" fill="#0255a3"/>
    <path d="M560 150 C470 175 420 260 300 296 C200 320 80 300 0 320 L0 314 C80 294 200 312 300 288 C420 252 470 166 560 140 Z" fill="#33a6d7"/>
  </svg>
  <div class="wordmark"><span class="mark-dot"></span>Tbm Welding &amp; Fabrication</div>
  <div class="divider"></div>
  <div class="contact">
    <p class="contact__name">Dale Hutchins</p>
    <p class="contact__line"><svg viewBox="0 0 24 24"><path d="M6.6 10.8a15 15 0 0 0 6.6 6.6l2.2-2.2c.3-.3.7-.4 1-.2 1.1.4 2.3.6 3.6.6.6 0 1 .4 1 1V20c0 .6-.4 1-1 1A17 17 0 0 1 3 4c0-.6.4-1 1-1h3.5c.6 0 1 .4 1 1 0 1.3.2 2.5.6 3.6.1.3 0 .7-.2 1z"/></svg>0438517264</p>
    <p class="contact__line"><svg viewBox="0 0 24 24"><path d="M2 5h20v14H2z M2 5l10 8 10-8" /></svg>dale@tbmweldingandfabrication.com.au</p>
    <p class="contact__line"><svg viewBox="0 0 24 24"><circle cx="12" cy="12" r="10"/></svg>www.tbmweldingandfabrication.com.au</p>
  </div>
  <div class="social"><span class="social__dot"></span>tbmweldingandfabrication</div>
</section>

<section class="card card--back" aria-label="Card back">
  <div class="flare" role="img" aria-label="Faint welding spark glow behind the name"></div>
  <div class="wordmark"><span class="mark-dot"></span>Tbm Welding<br>&amp; Fabrication</div>
  <div class="services-rule"></div>
  <div class="services-tag">What I do</div>
  <ul class="services">
    <li>Sheds and carports</li><li>Ute trays</li><li>Stockyards</li><li>Trailers</li><li>Farm equipment</li>
    <li>Stockcrates</li><li>Gateways and Entrances</li><li>Breakdowns</li><li>Maintenance</li><li>And lots more!</li>
  </ul>
</section>

</body>
</html>
```